Venta Laptop Cover Skin for a DJ

I’m a wedding/corporate DJ that’s looking to have a unique laptop skin design for my Quilto laptop.

I will like to have a laptop cover skin that is a creative combination of professional, uniqueness, timeliness and looks solid.

I will like someone to take my current logo to incorporate into the design and only change the bottom “Tagline” in the logo to my new tagline listed below in the same area as the current tag.
New Tag: DJ Services | Photo Booths | Event Lighting

3D Feel
½ of laptop design with info list above and ½ laptop design with TJK attached logo
Colors: Stick with colors in my logo
Professional Design
o Note: I used this laptop for meetings and for DJ Gigs
Fonts: Open
Company Colors: Maroon / white / black

I have added our logo as an attachment, as well as our current laptop design skin. We are looking for something totally different.

Additionally, I have attached a further description of what we will like included.

• Name: DuNN HoLT ( Name need to be BIG but not over bearing ) Company Name: TJK Entertainment 2nd Co Name: TJK Management Website: www.tjkentertainment-demo.net TJK Logo Attached: See attached file o Note: EPS or AI file format of the logo can be sent to winner of the design contest PX Name: MrTJK7000 Hashtag: #TJKEntertainment Folkspace Name: TJK Entertainment

```html
<!DOCTYPE html>
<html lang="en">
<head>
<meta charset="utf-8">
<title>DuNN HoLT – TJK Entertainment Laptop Skin</title>
<link rel="stylesheet" href="https://fonts.googleapis.com/css2?family=Montserrat:wght@400;500;600;700&family=Orbitron:wght@700;800&display=swap">
<style>
  :root {
    --page: #ffffff;
    --skin-black: #000000;
    --maroon: #8c1a1f;
    --maroon-deep: #5a0f12;
    --red: #d51c24;
    --white: #ffffff;
  }
  * { margin: 0; padding: 0; box-sizing: border-box; }
  html, body {
    width: 1200px;
    height: 1142px;
    overflow: hidden;
    background: var(--page);
  }
  .skin {
    position: absolute;
    left: 20px;
    top: 186px;
    width: 1160px;
    height: 769px;
    background: var(--skin-black);
    border-radius: 28px;
    overflow: hidden;
    font-family: "Montserrat", sans-serif;
    color: var(--white);
  }

  /* Brand block, top left */
  .brand {
    position: absolute;
    left: 60px;
    top: 70px;
    width: 300px;
  }
  .brand-mark {
    display: flex;
    align-items: center;
    gap: 14px;
    padding-left: 25px;
  }
  .brand-dot {
    width: 30px;
    height: 30px;
    border-radius: 50%;
    background: var(--maroon);
  }
  .brand-name {
    font-family: "Montserrat", sans-serif;
    font-weight: 700;
    font-size: 88px;
    line-height: 1;
    letter-spacing: 2px;
    color: var(--maroon);
  }
  .brand-tagline {
    position: absolute;
    left: 25px;
    top: 160px;
    white-space: nowrap;
    font-weight: 600;
    font-size: 10px;
    letter-spacing: 0.2px;
    color: var(--white);
  }

  /* Artwork area, lower left */
  .artwork {
    position: absolute;
    left: 25px;
    top: 268px;
    width: 530px;
    height: 481px;
    background:
      radial-gradient(ellipse 45% 55% at 50% 52%, rgba(213, 28, 36, 0.95) 0%, rgba(150, 20, 26, 0.7) 45%, rgba(0, 0, 0, 0) 100%),
      linear-gradient(to top, rgba(120, 16, 20, 0.55) 0%, rgba(0, 0, 0, 0) 70%);
  }

  /* Info column, right */
  .owner-name {
    position: absolute;
    left: 580px;
    width: 516px;
    top: 100px;
    font-family: "Orbitron", sans-serif;
    font-weight: 800;
    font-size: 66px;
    line-height: 1;
    letter-spacing: 1px;
    text-align: right;
    white-space: nowrap;
  }
  .band {
    position: absolute;
    left: 580px;
    width: 516px;
    background: linear-gradient(to right, var(--maroon) 0%, var(--maroon-deep) 55%, rgba(0, 0, 0, 0) 100%);
    display: flex;
    align-items: center;
    white-space: nowrap;
    overflow: hidden;
  }
  .band-companies {
    top: 199px;
    height: 49px;
    font-weight: 400;
    font-size: 24px;
    letter-spacing: 0.2px;
  }
  .band-companies .divider { margin: 0 14px 0 20px; }
  .band-website {
    top: 667px;
    height: 49px;
    padding-left: 4px;
    font-weight: 600;
    font-size: 28px;
    letter-spacing: 0;
  }

  .social-list {
    position: absolute;
    right: 64px;
    top: 447px;
    list-style: none;
  }
  .social-item {
    display: flex;
    align-items: center;
    justify-content: flex-end;
    height: 48px;
    margin-bottom: 15px;
  }
  .social-handle {
    font-weight: 600;
    font-size: 24px;
    letter-spacing: 0.3px;
    margin-right: 22px;
  }
  .social-badge {
    width: 44px;
    height: 44px;
    border-radius: 50%;
    background: linear-gradient(135deg, var(--red) 0%, var(--maroon-deep) 100%);
    display: flex;
    align-items: center;
    justify-content: center;
    font-weight: 700;
    font-size: 24px;
    color: var(--white);
  }
</style>
</head>
<body>
  <main class="skin">
    <div class="brand">
      <div class="brand-mark">
        <span class="brand-name">TJK</span>
        <span class="brand-dot"></span>
      </div>
      <p class="brand-tagline">DJ Services | Photo Booths | Event Lighting</p>
    </div>

    <div class="artwork" role="img" aria-label="Red DJ headphones in front of a red sound equalizer bar graphic"></div>

    <h1 class="owner-name">DuNN HoLT</h1>

    <p class="band band-companies">TJK Entertainment<span class="divider">/</span>TJK Management</p>

    <ul class="social-list">
      <li class="social-item">
        <span class="social-handle">MrTJK7000</span>
        <span class="social-badge" aria-label="PX"></span>
      </li>
      <li class="social-item">
        <span class="social-handle">TJKEntertainment</span>
        <span class="social-badge" aria-label="Hashtag">#</span>
      </li>
      <li class="social-item">
        <span class="social-handle">TJK Entertainment</span>
        <span class="social-badge" aria-label="Folkspace"></span>
      </li>
    </ul>

    <p class="band band-website">www.tjkentertainment-demo.net</p>
  </main>
</body>
</html>
```